Mastering the Art of Challenging Conversations

I need a professional powerpoint presentation to use when teaching corporate workshops about how to handle hard conversations. I want it to be colorful, but not cartoonish. The images I attached are from quellin snap photos - I like the colors and the look of the image with the people and the conversation and thought "bubbles" above their heads. I also like the image of the two conversation bubbles with heads inside the bubbles. The slides will not have a lot of text on them so the design will be prominent. I'm also open to the idea of stock photos showing people engaged in both frustrating and successful conversations.

Target Market(s)

Corporate Managers

Industry/Entity Type

Corporate Talent Development

Font styles to use
Sans Serif

Colors
0094D4
00A9DD
6FCCEA
C7EBF8
E9F6FB
F0912C
F2A743
F7CA91
FBE8D2
FDF5EE
6B429C
8869AF
B7A5CE
E3DAEB
F3F0F8

Requirements
Must have
• An uncluttered look - professional, but not stuffy. Colorful but not cartoonish,
Nice to have
• The presentation is all about how to have conversations. So conversation and thought bubbles should be used in the design but not overdone.
Should not have
• cartoons, clip art, patterns (only solid colors for fill in and backgrounds)

```html
<!DOCTYPE html>
<html lang="en">
<head>
<meta charset="utf-8">
<title>Mastering the Art of Challenging Conversations</title>
<link rel="stylesheet" href="https://fonts.googleapis.com/css2?family=Source+Sans+3:wght@400&display=swap">
<style>
  :root {
    --purple: #6B429C;
    --purple-deep: #6E4399;
    --rose: #BE6670;
    --orange: #EF7F2F;
    --white: #FFFFFF;
    --figure-tint: rgba(255, 255, 255, 0.16);
  }
  * { margin: 0; padding: 0; box-sizing: border-box; }
  html, body { width: 1200px; height: 675px; overflow: hidden; }
  .slide {
    position: relative;
    width: 1200px;
    height: 675px;
    overflow: hidden;
    background: linear-gradient(90deg, var(--purple-deep) 0%, var(--rose) 52%, var(--orange) 100%);
    font-family: "Source Sans 3", "Myriad Pro", Arial, sans-serif;
  }
  .speech-bubble {
    position: absolute;
    left: 0;
    top: 0;
    width: 1200px;
    height: 675px;
  }
  .speech-text {
    position: absolute;
    left: 466px;
    top: 136px;
    width: 370px;
    color: var(--purple);
    font-size: 22.5px;
    line-height: 27px;
    font-weight: 400;
  }
  .figure {
    position: absolute;
    top: 294px;
    width: 327px;
    height: 347px;
    background: var(--figure-tint);
    border-radius: 150px 150px 40px 10px;
  }
  .figure--speaker { left: 36px; }
  .figure--listener { left: 825px; border-radius: 150px 150px 10px 40px; }
</style>
</head>
<body>
  <main class="slide">
    <svg class="speech-bubble" viewBox="0 0 1200 675" aria-hidden="true">
      <ellipse cx="628" cy="190" rx="237.5" ry="142.5" fill="var(--white)"/>
      <polygon points="448,282 363,392 519,317 560,300 470,260" fill="var(--white)"/>
    </svg>
    <p class="speech-text">Lorem ipsum dolor sit amet, consectetur adipiscing elit, sed do eiusmod tempor incididunt ut labore et dolore magna aliqua.</p>
    <div class="figure figure--speaker" role="img" aria-label="White outline of a head in profile, facing right, speaking"></div>
    <div class="figure figure--listener" role="img" aria-label="White outline of a head in profile, facing left, with a thought cloud inside"></div>
  </main>
</body>
</html>
```